New Corporate Business Card - Velmorabelle

What we need:
We need a new corporate business card.
We want a new template that we can change by ourself.
We want business card modern and minimalist but that looks professional.
We will print it in 300 gr soft-touch.
Why not a white side with the logo and a red/grey side with the content?
Why not a grey side and a red side like our logo?
I am sure that you have better idea than ours that's the reason we come here.

Who we are:
We are a private label company in cosmetics based in Switzerland. We work in BtoB. We make skin care products for other brands.

Target Market(s)

B to B - Worldwide - any gender

Industry/Entity Type

Cosmetics

Contact Information for Business Card

Side 1:
Logo
Your Swiss Private Label Manufacturer or www.velmorabelle.ch

Side 2:
Name and surname (Example: Lucien Marchetaz)
Job Description (General Manager)
Telephone (+41 32 918 64 00)
Direct (+41 32 918 64 64)
Email (lucien.marchetaz@velmorabelle.ch)
Chemin des Prés-Fleuris 14, 2000 Neuchâtel, Switzerland
www.velmorabelle.ch

Font styles to use
Serif
Sans Serif

Requirements
Must have
• You can use 4 colors: white, red, grey and/or black .
Should not have
• Too much colors, too much things. We want it simple!

```html
<!DOCTYPE html>
<html lang="en">
<head>
<meta charset="utf-8">
<title>Velmorabelle – Business Card</title>
<link rel="stylesheet" href="https://fonts.googleapis.com/css2?family=Mulish:wght@400;500;600&display=swap">
<style>
  :root {
    --red: #c62f28;
    --red-light: #d24a40;
    --grey: #a9aaab;
    --grey-dark: #8f9193;
    --white: #ffffff;
    --stage: #dfe3e8;
    --stage-edge: #c3cad3;
    --font: "Mulish", "Helvetica Neue", Arial, sans-serif;
  }
  * { margin: 0; padding: 0; box-sizing: border-box; }
  html, body { width: 1200px; height: 675px; overflow: hidden; }
  body {
    font-family: var(--font);
    background: radial-gradient(ellipse at 40% 55%, #eef0f3 0%, var(--stage) 55%, var(--stage-edge) 100%);
    position: relative;
  }
  .card {
    position: absolute;
    top: 197px;
    width: 490px;
    height: 280px;
    border-radius: 3px;
    overflow: hidden;
    box-shadow: 0 14px 30px rgba(40, 50, 70, 0.18);
  }

  /* Front side */
  .card--front {
    left: 80px;
    background: linear-gradient(160deg, var(--red-light) 0%, var(--red) 70%);
    color: var(--white);
  }
  .front-brand {
    position: absolute;
    top: 92px; left: 0; right: 0;
    display: flex; align-items: center; justify-content: center; gap: 12px;
  }
  .brand-square {
    width: 18px; height: 18px;
    background: var(--white);
  }
  .brand-name {
    font-size: 34px;
    font-weight: 400;
    letter-spacing: 3px;
    color: var(--white);
  }
  .front-tagline {
    position: absolute;
    bottom: 44px; left: 0; right: 0;
    text-align: center;
    font-size: 14px;
    letter-spacing: 0.6px;
  }

  /* Back side */
  .card--back {
    left: 630px;
    background: var(--white);
    color: var(--red);
  }
  .back-brand {
    position: absolute;
    top: 28px; right: 30px;
    display: flex; align-items: center; gap: 8px;
  }
  .back-brand .brand-square { width: 12px; height: 12px; background: var(--red); }
  .back-brand .brand-name { font-size: 20px; letter-spacing: 2px; color: var(--red); }

  .contact-list {
    position: absolute;
    top: 112px; left: 30px;
    list-style: none;
    font-size: 11.5px;
    line-height: 18px;
  }
  .contact-list li { display: flex; align-items: center; gap: 8px; }
  .contact-list svg { width: 10px; height: 10px; flex: none; }
  .contact-list .icon-space { width: 10px; flex: none; }

  .card-bands {
    position: absolute;
    left: 0; bottom: 0;
    width: 490px; height: 90px;
  }
  .holder {
    position: absolute;
    left: 30px; bottom: 20px;
    color: var(--white);
  }
  .holder-name {
    font-size: 16px;
    font-weight: 500;
    letter-spacing: 0.6px;
    text-transform: uppercase;
  }
  .holder-role {
    font-size: 12px;
    letter-spacing: 2px;
    margin-top: 2px;
  }
  .address {
    position: absolute;
    right: 18px; bottom: 28px;
    display: flex; align-items: center; gap: 8px;
    color: var(--white);
    font-size: 10.5px;
    line-height: 14px;
  }
  .address svg { width: 11px; height: 14px; flex: none; }
</style>
</head>
<body>

  <section class="card card--front" aria-label="Business card front">
    <div class="front-brand">
      <span class="brand-square"></span>
      <span class="brand-name">Velmorabelle</span>
    </div>
    <p class="front-tagline">Your Swiss Private Label Manufacturer</p>
  </section>

  <section class="card card--back" aria-label="Business card back">
    <div class="back-brand">
      <span class="brand-square"></span>
      <span class="brand-name">Velmorabelle</span>
    </div>

    <ul class="contact-list">
      <li>
        <svg viewBox="0 0 10 10" aria-hidden="true"><path d="M2 0.8 L3.6 2.6 L2.8 3.6 C3.4 5 4.8 6.4 6.3 7.1 L7.3 6.3 L9.2 7.9 L8.2 9.3 C4.5 9 1 5.5 0.7 1.8 Z" fill="var(--grey-dark)"/></svg>
        <span>Tel. +41 32 918 64 00</span>
      </li>
      <li><span class="icon-space"></span><span>Direct. +41 32 918 64 64</span></li>
      <li>
        <svg viewBox="0 0 10 10" aria-hidden="true"><rect x="0.7" y="2" width="8.6" height="6" fill="none" stroke="var(--grey-dark)" stroke-width="0.9"/><path d="M0.7 2 L5 5.5 L9.3 2" fill="none" stroke="var(--grey-dark)" stroke-width="0.9"/></svg>
        <span>lucien.marchetaz@velmorabelle.ch</span>
      </li>
      <li>
        <svg viewBox="0 0 10 10" aria-hidden="true"><circle cx="5" cy="5" r="4.3" fill="none" stroke="var(--grey-dark)" stroke-width="0.9"/><ellipse cx="5" cy="5" rx="1.9" ry="4.3" fill="none" stroke="var(--grey-dark)" stroke-width="0.8"/><path d="M0.7 5 H9.3" stroke="var(--grey-dark)" stroke-width="0.8"/></svg>
        <span>www.velmorabelle.ch</span>
      </li>
    </ul>

    <svg class="card-bands" viewBox="0 0 490 90" aria-hidden="true">
      <rect x="300" y="12" width="190" height="78" fill="var(--grey)"/>
      <path d="M0 30 H245 C285 30 295 5 330 5 C352 5 362 30 372 90 H0 Z" fill="var(--red)"/>
    </svg>

    <div class="holder">
      <p class="holder-name">Lucien Marchetaz</p>
      <p class="holder-role">General Manager</p>
    </div>

    <div class="address">
      <svg viewBox="0 0 11 14" aria-hidden="true"><path d="M5.5 0.5 C2.7 0.5 0.7 2.5 0.7 5.1 C0.7 8.4 5.5 13.5 5.5 13.5 C5.5 13.5 10.3 8.4 10.3 5.1 C10.3 2.5 8.3 0.5 5.5 0.5 Z" fill="var(--white)"/><circle cx="5.5" cy="5.1" r="1.7" fill="var(--grey)"/></svg>
      <p>Chemin des Prés-Fleuris 14,<br>2000 Neuchâtel, Switzerland</p>
    </div>
  </section>

</body>
</html>
```